Group training gym/bootcamp needs a web design

We need a website for our gym that is based in Sydney. We have indoor functional training classes and outdoor bootcamp classes. We would like the web site to have a video (to be created) and photo gallery. I would like the site made on word press and i would like to be able to make minor changes such as changing images and text without having to use a designer.

The website should have the following pages: home page; the gym; the bootcamp; photo gallery; about us; contact.

I have uploaded our logo and i would like to keep to these colour (blue,yellow,silver) and black is also allowed

Target Market(s)

18-50 male and female

Industry/Entity Type

Gym

Coding

Coded - Design and coding required

Number of Pages Required

5+ page

Font styles to use
Sans Serif

Colors
0692cd
fbed22
1b1b1b
e8e8e8

Requirements
Must have
• The website should have the following pages: home page; the gym; the bootcamp; photo gallery; about us; contact.
• I have uploaded our logo and i would like to keep to these colour (blue,yellow,silver) and black is also allowed
• Video upload and photo upload

```html
<!DOCTYPE html>
<html lang="en">
<head>
<meta charset="utf-8">
<title>Corestrong Training Hub</title>
<link href="https://fonts.googleapis.com/css2?family=Montserrat:wght@400;500;600;700;800&display=swap" rel="stylesheet">
<style>
:root{
  --yellow:#fbed22;
  --blue:#0692cd;
  --ink:#1b1b1b;
  --silver:#e8e8e8;
  --black:#0e0e0e;
  --white:#ffffff;
  --grey:#555555;
}
*{box-sizing:border-box;margin:0;padding:0}
html,body{width:1200px;height:5128px;overflow:hidden}
body{font-family:"Montserrat",Arial,sans-serif;color:var(--ink);background:var(--white);position:relative}
.abs{position:absolute}
svg{display:block}

/* header / hero */
.hero{position:absolute;left:0;top:0;width:1200px;height:667px;background:linear-gradient(120deg,#1a1a1a 0%,#3a3a3a 45%,#151515 70%,#2e2e2e 100%);overflow:hidden}
.hero-deco{position:absolute;left:0;top:0}
.brand{position:absolute;left:96px;top:22px;display:flex;align-items:center;gap:12px}
.brand-mark{width:34px;height:34px;background:var(--yellow);border-radius:50%}
.brand-name{font-weight:800;font-size:19px;color:var(--white);letter-spacing:1px;text-transform:uppercase;line-height:1.1;width:150px}
.nav{position:absolute;right:80px;top:72px;display:flex;gap:40px}
.nav a{color:var(--white);text-decoration:none;font-size:15px;font-weight:600;text-transform:uppercase}
.nav a.is-active{color:var(--yellow)}
.hero-title{position:absolute;left:0;width:1200px;top:268px;text-align:center;color:var(--white)}
.hero-title small{display:block;font-size:15px;letter-spacing:3px;font-weight:500}
.hero-title h1{font-size:32px;font-weight:800;letter-spacing:2px;line-height:1.2;margin-top:10px;text-transform:uppercase}
.btn-yellow{display:inline-block;margin-top:24px;background:var(--yellow);color:var(--ink);font-weight:700;font-size:13px;padding:10px 26px;border-radius:22px;text-transform:uppercase}

/* section titles */
.sec-title{position:absolute;left:0;width:1200px;text-align:center}
.sec-title .ghost{font-size:62px;font-weight:800;color:rgba(0,0,0,.07);letter-spacing:2px;text-transform:uppercase;line-height:1}
.sec-title h2{font-size:27px;font-weight:800;text-transform:uppercase;margin-top:-40px;letter-spacing:1px}
.sec-title.on-dark .ghost{color:rgba(255,255,255,.08)}
.sec-title.on-dark h2{color:var(--white)}

/* about */
.about-ghost{position:absolute;left:85px;top:734px;font-size:62px;font-weight:800;color:rgba(0,0,0,.07);text-transform:uppercase}
.about-title{position:absolute;left:85px;top:758px;font-size:27px;font-weight:800;text-transform:uppercase}
.about-text{position:absolute;left:85px;top:832px;width:480px;font-size:13.5px;line-height:1.55;color:var(--grey)}
.about-text p{margin-bottom:22px}
.photo{position:absolute;background:linear-gradient(160deg,#6b5a48,#2b2520)}

/* video */
.video{position:absolute;left:0;top:1282px;width:1200px;height:564px;background:linear-gradient(90deg,#2c2c2c,#151515 35%,#111 65%,#2a2a2a)}
.video-label{position:absolute;left:0;width:1200px;top:1598px;text-align:center;color:var(--white);font-weight:800;font-size:27px;text-transform:uppercase}

/* portfolio */
.tile{position:absolute}
.tile-caption{position:absolute;left:0;right:0;text-align:center;color:var(--white);font-size:15px}

/* classes */
.classes{position:absolute;left:0;top:2838px;width:1200px;height:581px;background:linear-gradient(180deg,#2a2a2a,#101010)}
.class-card{position:absolute;width:300px;text-align:center}
.class-card h3{font-size:19px;font-weight:700;color:var(--white)}
.class-card p{font-size:13px;line-height:1.45;color:#d8d8d8;margin-top:14px;padding:0 30px}
.class-card.is-featured h3{color:var(--ink)}
.class-card.is-featured p{color:var(--ink)}

/* trainers */
.trainer-name{position:absolute;left:0;width:1200px;top:4112px;text-align:center;font-weight:700;font-size:16px;letter-spacing:1px;text-transform:uppercase}
.socials{display:flex;gap:6px}
.socials span{width:26px;height:26px;border-radius:50%;background:var(--blue)}

/* map & footer */
.map{position:absolute;left:0;top:4240px;width:1200px;height:376px;background:linear-gradient(135deg,#cfdde6,#e7ece5 50%,#c9d9e4)}
.footer{position:absolute;left:0;top:4616px;width:1200px;height:512px;background:var(--ink)}
.foot-brand{position:absolute;left:90px;top:4680px;display:flex;align-items:center;gap:10px}
.foot-brand .brand-name{font-size:15px;color:#bbb;width:140px}
.foot-text{position:absolute;left:90px;top:4780px;width:220px;font-size:12.5px;line-height:1.5;color:#9a9a9a}
.contact-box{position:absolute;left:376px;top:4513px;width:444px;height:513px;background:var(--yellow);padding:0 40px}
.contact-box .ghost{position:absolute;left:0;width:444px;top:20px;text-align:center;font-size:50px;font-weight:800;color:rgba(0,0,0,.08);text-transform:uppercase}
.contact-box h2{position:absolute;left:0;width:444px;top:44px;text-align:center;font-size:25px;font-weight:800;text-transform:uppercase}
.field{position:absolute;border-bottom:1px solid rgba(255,255,255,.9);font-size:13px;padding-bottom:8px}
.btn-send{position:absolute;left:154px;top:436px;width:136px;height:38px;background:var(--ink);color:var(--white);border-radius:20px;font-size:13px;font-weight:700;display:flex;align-items:center;justify-content:center;gap:8px;text-transform:uppercase}
.info{position:absolute;left:872px;color:var(--white)}
.info h4{font-size:13px;font-weight:700;text-transform:uppercase;display:flex;align-items:center;gap:12px}
.info p{font-size:13px;color:#aaa;margin:6px 0 0 32px;line-height:1.45}
.copyright{position:absolute;left:0;width:1200px;top:5070px;text-align:center;font-size:12px;color:#888}
</style>
</head>
<body>

<!-- HERO -->
<header class="hero">
  <div class="abs" role="img" aria-label="Athlete lifting a barbell in a dark gym" style="left:120px;top:120px;width:560px;height:547px;background:radial-gradient(ellipse at 50% 60%,#4a4a4a,rgba(20,20,20,0) 70%)"></div>
  <div class="abs" role="img" aria-label="Close-up of a muscular athlete's shoulder" style="left:820px;top:0;width:380px;height:667px;background:linear-gradient(200deg,#5a5a5a,#1c1c1c)"></div>
  <svg class="hero-deco" width="1200" height="667" viewBox="0 0 1200 667">
    <polyline points="80,0 215,130 120,230" fill="none" stroke="rgba(255,255,255,.5)" stroke-width="2"/>
    <polygon points="600,190 770,360 600,530 430,360" fill="rgba(0,0,0,.55)" stroke="rgba(255,255,255,.6)" stroke-width="2"/>
    <line x1="1200" y1="10" x2="700" y2="667" stroke="rgba(255,255,255,.7)" stroke-width="2"/>
    <line x1="1200" y1="80" x2="800" y2="667" stroke="rgba(255,255,255,.35)" stroke-width="2"/>
  </svg>
  <div class="brand"><span class="brand-mark"></span><span class="brand-name">Corestrong Training Hub</span></div>
  <nav class="nav">
    <a class="is-active">Home</a><a>About Us</a><a>The Gym</a><a>The Bootcamp</a><a>Photo Gallery</a><a>Contact</a>
  </nav>
  <div class="hero-title">
    <small>WELCOME TO</small>
    <h1>Corestrong<br>Training Hub</h1>
    <span class="btn-yellow">Go to Fitness</span>
  </div>
</header>

<!-- ABOUT -->
<section class="about">
  <svg class="abs" style="left:0;top:740px" width="90" height="460"><polygon points="0,0 85,230 0,460" fill="var(--yellow)"/></svg>
  <svg class="abs" style="left:650px;top:700px" width="550" height="580">
    <polygon points="300,20 560,290 300,560 40,290" fill="none" stroke="var(--yellow)" stroke-width="2"/>
    <polygon points="530,140 550,140 550,440 530,440" fill="none"/>
  </svg>
  <div class="about-ghost">Corestrong</div>
  <h2 class="about-title">About Us</h2>
  <div class="about-text">
    <p>Lorem Ipsum is simply dummy text of the printing and typesetting industry. Lorem Ipsum has been the industry's standard dummy text ever since the 1500s, when an unknown printer took a galley of type and scrambled it to make a type specimen book. It has survived not only five centuries, but also the leap into electronic typesetting, remaining essentially unchanged.</p>
    <p>Lorem Ipsum is simply dummy text of the printing and typesetting industry. Lorem Ipsum has been the industry's standard dummy text ever since the 1500s, when an unknown.</p>
    <p>Lorem Ipsum is simply dummy text of the printing and typesetting industry. Lorem Ipsum has been the industry's standard dummy text ever since the 1500s when an unknown printer took a galley of type and scrambled it to make.</p>
  </div>
  <div class="photo" role="img" aria-label="Athlete in a yellow tank top curling a dumbbell" style="left:728px;top:786px;width:322px;height:394px"></div>
</section>

<!-- VIDEO -->
<section class="video" role="img" aria-label="Woman and man training with dumbbells on a dark background"></section>
<svg class="abs" style="left:370px;top:1343px" width="460" height="460">
  <polygon points="230,0 460,230 230,460 0,230" fill="rgba(0,0,0,.35)" stroke="var(--yellow)" stroke-width="2"/>
  <rect x="195" y="170" width="70" height="70" rx="4" fill="none" stroke="var(--white)" stroke-width="3"/>
  <polygon points="218,188 218,222 248,205" fill="var(--yellow)"/>
</svg>
<div class="video-label">Watch Video</div>

<!-- PORTFOLIO -->
<section class="portfolio">
  <svg class="abs" style="left:1080px;top:1846px" width="120" height="240"><polygon points="120,0 0,110 120,240" fill="var(--yellow)"/></svg>
  <div class="sec-title" style="top:1920px"><div class="ghost">Corestrong</div><h2>Portfolio</h2></div>
  <div class="tile photo" role="img" aria-label="Smiling group on exercise bikes" style="left:85px;top:2024px;width:325px;height:448px;background:linear-gradient(150deg,#d9c7b8,#9e8f86)"></div>
  <div class="tile photo" role="img" aria-label="Women stretching on mats in a studio" style="left:438px;top:2024px;width:321px;height:267px;background:linear-gradient(150deg,#8fc5d9,#d6c2b0)"></div>
  <div class="tile photo" role="img" aria-label="Man working out on a cable machine" style="left:790px;top:2024px;width:321px;height:448px;background:linear-gradient(150deg,#9a8a7e,#4b4440)"></div>
  <div class="tile photo" role="img" aria-label="Group doing sit-ups on mats" style="left:85px;top:2503px;width:325px;height:266px;background:linear-gradient(150deg,#b9aea6,#6b6562)"></div>
  <div class="tile photo" role="img" aria-label="Athlete in dark light with overlay" style="left:438px;top:2318px;width:321px;height:451px;background:linear-gradient(160deg,#3a3535,#151515)"></div>
  <svg class="abs" style="left:498px;top:2444px" width="200" height="200">
    <polygon points="100,0 200,100 100,200 0,100" fill="none" stroke="var(--yellow)" stroke-width="2"/>
    <rect x="88" y="70" width="22" height="20" fill="none" stroke="var(--yellow)" stroke-width="2.5"/>
    <line x1="100" y1="80" x2="114" y2="66" stroke="var(--yellow)" stroke-width="2.5"/>
  </svg>
  <div class="tile-caption" style="left:438px;width:321px;top:2550px">Lorem ipsume</div>
  <div class="tile photo" role="img" aria-label="Man doing push-ups on kettlebells" style="left:790px;top:2503px;width:321px;height:266px;background:linear-gradient(180deg,#7fc3e6,#b8b0a6)"></div>
</section>

<!-- CLASSES -->
<section class="classes" role="img" aria-label="Dim gym interior with treadmills"></section>
<div class="sec-title on-dark" style="top:2908px"><div class="ghost">Corestrong</div><h2>Our Classes</h2></div>
<svg class="abs" style="left:0;top:3020px" width="1200" height="330">
  <polygon points="250,10 400,160 250,310 100,160" fill="rgba(0,0,0,.35)" stroke="var(--yellow)" stroke-width="2"/>
  <polygon points="600,0 760,160 600,320 440,160" fill="var(--yellow)"/>
  <polygon points="968,10 1118,160 968,310 818,160" fill="rgba(0,0,0,.35)" stroke="var(--yellow)" stroke-width="2"/>
  <circle cx="250" cy="80" r="10" fill="var(--yellow)"/>
  <circle cx="600" cy="80" r="10" fill="var(--ink)"/>
  <circle cx="968" cy="80" r="10" fill="var(--yellow)"/>
  <circle cx="250" cy="250" r="4" fill="var(--yellow)"/>
  <circle cx="600" cy="250" r="4" fill="var(--ink)"/>
  <circle cx="968" cy="250" r="4" fill="var(--yellow)"/>
  <polygon points="40,160 52,152 52,168" fill="var(--white)"/>
  <polygon points="1160,160 1148,152 1148,168" fill="var(--yellow)"/>
</svg>
<div class="class-card" style="left:100px;top:3130px"><h3>Fitness Classes</h3><p>Lorem Ipsum is simply dummy text of the printing and typesetting industry.</p></div>
<div class="class-card is-featured" style="left:450px;top:3130px"><h3>Yoga Classes</h3><p>Lorem Ipsum is simply dummy text of the printing and typesetting industry.</p></div>
<div class="class-card" style="left:818px;top:3130px"><h3>Boxing Classes</h3><p>Lorem Ipsum is simply dummy text of the printing and typesetting industry.</p></div>

<!-- TRAINERS -->
<section class="trainers">
  <svg class="abs" style="left:0;top:3419px" width="1200" height="821">
    <polygon points="0,0 100,0 0,200" fill="var(--yellow)"/>
    <polygon points="1200,250 1200,821 880,821" fill="var(--yellow)"/>
    <polygon points="600,154 856,410 600,666 344,410" fill="none" stroke="var(--yellow)" stroke-width="2"/>
  </svg>
  <div class="sec-title" style="top:3460px"><div class="ghost">Corestrong</div><h2>Trainers</h2></div>
  <svg class="abs" style="left:0;top:3600px" width="1200" height="480">
    <defs>
      <linearGradient id="tg" x1="0" y1="0" x2="1" y2="1"><stop offset="0" stop-color="#6a6a6a"/><stop offset="1" stop-color="#d8d8d8"/></linearGradient>
      <linearGradient id="tm" x1="0" y1="0" x2="1" y2="1"><stop offset="0" stop-color="#c9b3a4"/><stop offset="1" stop-color="#a3202a"/></linearGradient>
    </defs>
    <polygon points="240,60 410,230 240,400 70,230" fill="url(#tg)" role="img" aria-label="Trainer portrait in black and white"/>
    <polygon points="957,60 1127,230 957,400 787,230" fill="url(#tg)" role="img" aria-label="Trainer portrait in black and white"/>
    <polygon points="600,0 830,230 600,460 370,230" fill="url(#tm)" role="img" aria-label="Trainer coaching a client with dumbbells"/>
    <polygon points="240,380 256,398 224,398" fill="var(--grey)" transform="rotate(180 240 389)"/>
    <text x="40" y="235" font-size="10" fill="#bbb" font-family="Montserrat, sans-serif">PREV</text>
  </svg>
  <div class="trainer-name">Marcus Hale</div>
  <div class="socials abs" style="left:560px;top:4145px"><span></span><span></span><span></span></div>
</section>

<!-- MAP -->
<section class="map" role="img" aria-label="Street map of the gym's neighbourhood"></section>
<svg class="abs" style="left:586px;top:4375px" width="28" height="40">
  <path d="M14 0C6 0 0 6 0 14c0 10 14 26 14 26s14-16 14-26C28 6 22 0 14 0z" fill="#d32f2f"/><circle cx="14" cy="14" r="5" fill="#fff"/>
</svg>

<!-- FOOTER -->
<footer class="footer"></footer>
<div class="foot-brand"><span class="brand-mark" style="background:#777"></span><span class="brand-name">Corestrong Training Hub</span></div>
<div class="foot-text">Lorem Ipsum is simply dummy text of the printing and typesetting industry. Lorem Ipsum is simply dummy text of the printing and typesetting industry.</div>

<div class="contact-box">
  <div class="ghost">Corestrong</div>
  <h2>Contact Us</h2>
  <div class="field" style="left:40px;top:160px;width:364px">Name</div>
  <div class="field" style="left:40px;top:230px;width:170px">Email</div>
  <div class="field" style="left:234px;top:230px;width:170px">Phone</div>
  <div class="field" style="left:40px;top:300px;width:364px;height:100px">Message</div>
  <div class="btn-send"><svg width="14" height="14"><polygon points="0,2 14,7 0,12 3,7" fill="#fff"/></svg>Send</div>
</div>

<div class="info" style="top:4680px">
  <h4><svg width="18" height="18"><path d="M4 1l3 4-2 2c1 2 3 4 5 5l2-2 4 3-2 4C8 17 1 10 0 4z" fill="var(--yellow)"/></svg>Telephone</h4>
  <p>02 5550 1847</p>
</div>
<div class="info" style="top:4760px">
  <h4><svg width="18" height="14"><rect width="18" height="14" rx="2" fill="var(--yellow)"/><polyline points="1,2 9,8 17,2" fill="none" stroke="var(--ink)" stroke-width="1.5"/></svg>Email</h4>
  <p>hello@corestronghub.com</p>
</div>
<div class="info" style="top:4840px">
  <h4><svg width="18" height="18"><path d="M9 0C5 0 2 3 2 7c0 5 7 11 7 11s7-6 7-11C16 3 13 0 9 0z" fill="var(--yellow)"/><circle cx="9" cy="7" r="2.5" fill="var(--ink)"/></svg>Address</h4>
  <p>48 Harbour Lane,<br>Sydney NSW</p>
</div>
<div class="socials abs" style="left:872px;top:4940px"><span></span><span></span><span></span></div>

<div class="copyright">© 2017 Corestrong Training Hub. All Rights Reserved</div>
<svg class="abs" style="left:1100px;top:5042px" width="40" height="40"><polygon points="20,0 40,20 20,40 0,20" fill="var(--yellow)"/><polyline points="14,23 20,17 26,23" fill="none" stroke="var(--ink)" stroke-width="2"/></svg>

</body>
</html>
```